Leave-behind marketing postcard showing retirement plan limits for the last three years.

We need a 5x7 postcard for our company, Meridel Halvorsen, Inc. We are a third party retirement plan administration firm. The piece should include our logo, address, phone, website, and the contribution limits for the last three years - 2015, 2014, 2013 (see attached for company logo, color palette and retirement plan limits chart). You can also incorporate our slogan on one of the sides - "Providing and protecting retirement since 1983." This postcard is a leave-behind. We will not be mailing it so you don't have to include space for a stamp and address. The postcard can be 4 color on both sides. Include a bleed.

Target Market(s)

Financial advisors and business owners

Industry/Entity Type

Marketing

Font styles to use
Other font styles liked:
• Georgia and arial

Requirements
Must have
• Please use some of the colors in the attached color palette.

```html
<!DOCTYPE html>
<html lang="en">
<head>
<meta charset="utf-8">
<title>Meridel Halvorsen, Inc. – Retirement Plan Limits Postcard</title>
<link href="https://fonts.googleapis.com/css2?family=Arimo:wght@400;700&family=Gelasio:wght@400;700&display=swap" rel="stylesheet">
<style>
  :root{
    --navy:#16205a;
    --navy-deep:#0d1a4f;
    --teal:#72b7c4;
    --cell-gray:#d4d4d6;
    --head-gray:#8c8483;
    --rule:#9a9a9a;
    --text-gray:#333;
    --paper:#ffffff;
    --canvas:#ffffff;
  }
  *{box-sizing:border-box;margin:0;padding:0}
  html,body{width:813px;height:1200px;overflow:hidden;background:var(--canvas)}
  body{position:relative;font-family:"Arimo",Arial,sans-serif;color:var(--navy)}
  .card{position:absolute;left:0;width:813px;background:var(--paper);border:1px solid #b9b9b9;overflow:hidden}
  .card--front{top:0;height:594px}
  .card--back{top:623px;height:577px}

  .brand{position:absolute;left:32px;top:40px;width:300px;font-family:"Gelasio",Georgia,serif;
    font-weight:700;font-size:34px;line-height:1.1;color:var(--navy)}
  .slogan{position:absolute;left:320px;width:440px;top:36px;text-align:center;
    font-family:"Gelasio",Georgia,serif;font-size:35px;line-height:45px;color:var(--navy)}

  .photo{position:absolute;left:0;width:100%}
  .photo--road{top:181px;height:222px;
    background:linear-gradient(180deg,#3d5b82 0%,#c9a468 48%,#efe0b0 55%,#a88b4e 62%,#3d3a33 100%)}
  .photo-rule{position:absolute;left:0;top:403px;width:100%;height:8px;background:var(--navy-deep)}

  .intro{position:absolute;left:40px;right:40px;top:420px;text-align:center;
    font-size:19.5px;line-height:24px;color:var(--navy)}

  .divider{position:absolute;left:0;width:813px;height:30px}
  .card--front .divider{top:490px}
  .card--back .divider{top:490px}

  .contact{position:absolute;left:32px;font-size:14px;line-height:19px;color:var(--text-gray)}
  .card--front .contact{top:524px}
  .card--back .contact{top:524px}
  .web{position:absolute;right:30px;font-weight:700;font-size:22px;color:var(--navy)}
  .card--front .web{top:518px}
  .card--back .web{top:518px}

  .photo--pier{top:0;height:127px;
    background:linear-gradient(180deg,#1c3559 0%,#5f86ad 45%,#c7d7e6 62%,#7fa2c4 80%,#355878 100%)}
  .banner-name{position:absolute;right:24px;top:16px;font-size:15px;letter-spacing:3px;
    color:#fff;font-weight:400}

  .limits-title{position:absolute;left:45px;top:132px;font-family:"Gelasio",Georgia,serif;
    font-weight:700;font-size:24px;line-height:30px;color:var(--navy)}
  .limits{position:absolute;left:45px;top:164px;width:723px;border-collapse:collapse;
    font-size:17.5px}
  .limits th,.limits td{border:1.5px solid #fff;height:31px;padding:0 6px;line-height:20px}
  .limits thead th{height:24px;background:var(--head-gray);color:#fff;font-weight:700;text-align:center}
  .limits thead th:first-child{text-align:left}
  .limits tbody th{background:var(--navy-deep);color:#fff;text-align:left;font-weight:700;width:378px}
  .limits td{text-align:center;color:#111;background:var(--cell-gray);width:115px}
  .limits td.y2014{background:var(--teal)}
  .limits sup,.footnotes sup{font-size:10px;line-height:0}
  .footnotes{position:absolute;left:45px;top:442px;font-size:12px;line-height:14px;color:#111}
</style>
</head>
<body>

<section class="card card--front">
  <div class="brand">Meridel Halvorsen, Inc.</div>
  <p class="slogan">Providing and protecting retirement since 1983.</p>
  <div class="photo photo--road" role="img" aria-label="Open highway stretching to a sunset horizon across golden plains"></div>
  <div class="photo-rule"></div>
  <p class="intro">We are a highly experienced Third Party Administration firm that handles all aspects of your company’s retirement plan, except the investments. As consultants, we help to strategically design your plan, saving you time and money.</p>
  <svg class="divider" viewBox="0 0 813 30" aria-hidden="true">
    <path d="M0 28 H505 C525 28 525 8 545 8 H813" fill="none" stroke="var(--rule)" stroke-width="1.5"/>
  </svg>
  <p class="contact">1840 Harbor Crest Ave., Suite 210 Lomita, CA 90717<br>Phone 310.555.0142 &nbsp;&nbsp; Fax 310.555.0148</p>
  <p class="web">www.mhbenefits.com</p>
</section>

<section class="card card--back">
  <div class="photo photo--pier" role="img" aria-label="Wooden pier leading to a lit pavilion over calm water at dusk"></div>
  <span class="banner-name">MERIDEL HALVORSEN, INC.</span>
  <h2 class="limits-title">Maximum Benefit and Contribution Limits</h2>
  <table class="limits">
    <thead>
      <tr><th>Type of Limitation</th><th>2015</th><th>2014</th><th>2013</th></tr>
    </thead>
    <tbody>
      <tr><th>401(k) / 403(b) Elective Deferrals</th><td>$18,000</td><td class="y2014">$17,500</td><td>$17,500</td></tr>
      <tr><th>Catch-up amount<sup>*</sup></th><td>$6,000</td><td class="y2014">$5,500</td><td>$5,500</td></tr>
      <tr><th>Defined Benefit Plans<sup>1</sup></th><td>$210,000</td><td class="y2014">$210,000</td><td>$205,000</td></tr>
      <tr><th>Defined Contribution Plans<sup>1</sup></th><td>$53,000</td><td class="y2014">$52,000</td><td>$51,000</td></tr>
      <tr><th>Annual Compensation Limit<sup>2</sup></th><td>$265,000</td><td class="y2014">$260,000</td><td>$255,000</td></tr>
      <tr><th>Highly Compensated Employees</th><td>$120,000</td><td class="y2014">$115,000</td><td>$115,000</td></tr>
      <tr><th>Key employee officer threshold<sup>1</sup></th><td>$170,000</td><td class="y2014">$170,000</td><td>$165,000</td></tr>
      <tr><th>Income Subject to Social Security Tax<sup>2</sup></th><td>$118,500</td><td class="y2014">$117,000</td><td>$113,700</td></tr>
    </tbody>
  </table>
  <p class="footnotes">*For individuals age 50 and older<br><sup>1</sup> Based on plan year ending in calendar year<br><sup>2</sup> Based on plan year beginning in calendar year</p>
  <svg class="divider" viewBox="0 0 813 30" aria-hidden="true">
    <path d="M0 28 H505 C525 28 525 8 545 8 H813" fill="none" stroke="var(--rule)" stroke-width="1.5"/>
  </svg>
  <p class="contact">1840 Harbor Crest Ave., Suite 210 Lomita, CA 90717<br>Phone 310.555.0142 &nbsp;&nbsp; Fax 310.555.0148</p>
  <p class="web">www.mhbenefits.com</p>
</section>

</body>
</html>
```